Cultural Values, and Purpose, Vision and Mission statements design

We have recently created Cultural Values, and Purpose, Vision and Mission statements for a client’s business. We would like a visual representation created of each of these, to be hung on display in their office. For this project, we would like four (4) graphic design prints drawn up that depict:1. Purpose2. Vision3. Mission4. Cultural ValuesAll print designs should use a recurring, common theme, and be reflective of the business’ colours (see attached logo.)Please read and follow specifications in attached design brief.
Updates

Need extra days to review

Target Market(s)

Females, aged between 37 and 57 years old, who are family orientated, living locally, married and have between 1 and 3 children living at home.

Requirements
Must have
• Photoshop (PSD) format: All completed design will need to be in Photoshop (PSD) format before being handed over. This is to ensure that we can make alterations before printing if necessary.
• Quality: All designs must be 300 pixels resolution or higher.
• Purpose, Vision & Mission Designs Dimensions: The dimensions for each of the Purpose, Vision and Mission designs will need to be 30.5cm x 40.6cm (portrait, rectangle shape) with a surrounding 3.8cm border as it will be printed onto canvas matching these specifications.
• Cultural Values Dimensions: There are no specific dimensions required for the Cultural Values so the designer should feel free to display them best they see fit.
• Theme: All must follow the same theme and be reflective of the business's colours and logo.

```html
<!DOCTYPE html>
<html lang="en">
<head>
<meta charset="utf-8">
<title>Wrenford – Purpose, Vision, Mission and Cultural Values</title>
<link rel="stylesheet" href="https://fonts.googleapis.com/css2?family=Poppins:wght@400;500;600;700&family=Roboto:wght@500;700&display=swap">
<style>
  :root {
    --orange: #f38120;
    --gray: #939598;
    --white: #ffffff;
    --title-light: #f1f1f2;
    --page: #ffffff;
  }
  html, body {
    margin: 0;
    padding: 0;
    width: 960px;
    height: 1200px;
    overflow: hidden;
    background: var(--page);
  }
  .sheet { position: relative; width: 960px; height: 1200px; }
  .poster { position: absolute; width: 394px; height: 524px; display: block; }
  .poster--purpose { left: 62px;  top: 56px; }
  .poster--vision  { left: 504px; top: 56px; }
  .poster--mission { left: 62px;  top: 619px; }
  .poster--values  { left: 504px; top: 619px; }

  .fill-orange { fill: var(--orange); }
  .fill-gray   { fill: var(--gray); }
  .fill-white  { fill: var(--white); }
  .frame { fill: none; stroke: var(--orange); stroke-width: 3; }

  .brand-name {
    font-family: "Poppins", sans-serif;
    font-weight: 600;
    font-size: 40px;
    fill: var(--orange);
  }
  .brand-tagline {
    font-family: "Poppins", sans-serif;
    font-weight: 400;
    font-size: 13px;
    fill: var(--gray);
  }
  .statement-title {
    font-family: "Poppins", sans-serif;
    font-weight: 700;
    font-size: 32px;
    fill: var(--orange);
  }
  .statement-body {
    font-family: "Poppins", sans-serif;
    font-weight: 400;
    font-size: 25px;
    fill: var(--white);
  }
  .statement-body--long { font-size: 19px; }

  .value-label {
    font-family: "Roboto", sans-serif;
    font-weight: 500;
    font-size: 25px;
    fill: var(--white);
  }
  .values-title {
    font-family: "Roboto", sans-serif;
    font-weight: 700;
    font-size: 35px;
    letter-spacing: 1px;
    fill: var(--title-light);
  }
  .connector { stroke: var(--gray); stroke-width: 14; stroke-linecap: round; fill: none; }
  .ring { fill: var(--white); stroke: var(--gray); stroke-width: 9; }
</style>
</head>
<body>
<main class="sheet">

  <!-- Purpose -->
  <svg class="poster poster--purpose" viewBox="0 0 492 655" xmlns="http://www.w3.org/2000/svg">
    <defs>
      <linearGradient id="artTone" x1="0" y1="0" x2="1" y2="1">
        <stop offset="0" stop-color="#f38120"/>
        <stop offset="1" stop-color="#939598"/>
      </linearGradient>
    </defs>
    <rect class="fill-white" width="492" height="655"/>
    <polygon class="fill-gray" points="0,0 250,0 228,22 0,22"/>
    <polygon class="fill-orange" points="262,0 492,0 492,22 240,22"/>
    <rect class="fill-gray" x="120" y="84" width="52" height="52"/>
    <text class="brand-name" x="196" y="116">Wrenford</text>
    <text class="brand-tagline" x="198" y="135">Trusted care on local roads</text>

    <text class="statement-title" x="10" y="308">PURPOSE</text>
    <path class="fill-orange" d="M0,310 H185 Q200,310 212,322 L420,515 Q450,540 480,515 L492,505 V612 H0 Z"/>
    <polygon class="fill-white" points="0,582 386,582 378,592 0,592"/>
    <polygon class="fill-gray" points="492,502 492,655 0,655 0,612 377,612"/>
    <rect x="288" y="240" width="190" height="170" rx="18" fill="url(#artTone)" role="img" aria-label="Car with shield and tick illustration"/>

    <text class="statement-body">
      <tspan x="12" y="436">Providing vehicle</tspan>
      <tspan x="12" y="465">safety and security to</tspan>
      <tspan x="12" y="493">Westvale families on</tspan>
      <tspan x="12" y="521">our country roads.</tspan>
    </text>
    <rect class="frame" x="1.5" y="1.5" width="489" height="652"/>
  </svg>

  <!-- Vision -->
  <svg class="poster poster--vision" viewBox="0 0 492 655" xmlns="http://www.w3.org/2000/svg">
    <rect class="fill-white" width="492" height="655"/>
    <polygon class="fill-gray" points="0,0 250,0 228,22 0,22"/>
    <polygon class="fill-orange" points="262,0 492,0 492,22 240,22"/>
    <rect class="fill-gray" x="120" y="84" width="52" height="52"/>
    <text class="brand-name" x="196" y="116">Wrenford</text>
    <text class="brand-tagline" x="198" y="135">Trusted care on local roads</text>

    <text class="statement-title" x="10" y="308">VISION</text>
    <path class="fill-orange" d="M0,310 H185 Q200,310 212,322 L420,515 Q450,540 480,515 L492,505 V612 H0 Z"/>
    <polygon class="fill-white" points="0,582 386,582 378,592 0,592"/>
    <polygon class="fill-gray" points="492,502 492,655 0,655 0,612 377,612"/>
    <rect x="288" y="240" width="190" height="170" rx="18" fill="url(#artTone)" role="img" aria-label="Car with shield and family illustration"/>

    <text class="statement-body">
      <tspan x="12" y="406">We will earn our</tspan>
      <tspan x="12" y="434">reputation for being</tspan>
      <tspan x="12" y="463">the number one, family</tspan>
      <tspan x="12" y="491">focused, automotive</tspan>
      <tspan x="12" y="519">specialists throughout</tspan>
      <tspan x="12" y="547">the Marlow Valley.</tspan>
    </text>
    <rect class="frame" x="1.5" y="1.5" width="489" height="652"/>
  </svg>

  <!-- Mission -->
  <svg class="poster poster--mission" viewBox="0 0 492 655" xmlns="http://www.w3.org/2000/svg">
    <rect class="fill-white" width="492" height="655"/>
    <polygon class="fill-gray" points="0,0 250,0 228,22 0,22"/>
    <polygon class="fill-orange" points="262,0 492,0 492,22 240,22"/>
    <rect class="fill-gray" x="120" y="84" width="52" height="52"/>
    <text class="brand-name" x="196" y="116">Wrenford</text>
    <text class="brand-tagline" x="198" y="135">Trusted care on local roads</text>

    <text class="statement-title" x="10" y="308">MISSION</text>
    <path class="fill-orange" d="M0,310 H185 Q200,310 212,322 L420,515 Q450,540 480,515 L492,505 V612 H0 Z"/>
    <polygon class="fill-white" points="0,582 386,582 378,592 0,592"/>
    <polygon class="fill-gray" points="492,502 492,655 0,655 0,612 377,612"/>
    <rect x="288" y="240" width="190" height="170" rx="18" fill="url(#artTone)" role="img" aria-label="Car with shield and handshake illustration"/>

    <text class="statement-body statement-body--long">
      <tspan x="12" y="374">Through the delivery</tspan>
      <tspan x="12" y="398">of high-quality automotive</tspan>
      <tspan x="12" y="423">services and customer</tspan>
      <tspan x="12" y="447">experience excellence, we will</tspan>
      <tspan x="12" y="472">instil confidence and security</tspan>
      <tspan x="12" y="496">into our clients. We will build a</tspan>
      <tspan x="12" y="521">solid platform of trust in which</tspan>
      <tspan x="12" y="545">our entire industry will recognise</tspan>
      <tspan x="12" y="569">the benefits.</tspan>
    </text>
    <rect class="frame" x="1.5" y="1.5" width="489" height="652"/>
  </svg>

  <!-- Cultural Values -->
  <svg class="poster poster--values" viewBox="0 0 492 655" xmlns="http://www.w3.org/2000/svg">
    <defs>
      <linearGradient id="iconTone" x1="0" y1="0" x2="1" y2="1">
        <stop offset="0" stop-color="#f38120"/>
        <stop offset="1" stop-color="#f6a25c"/>
      </linearGradient>
    </defs>
    <rect class="fill-white" width="492" height="655"/>
    <polygon class="fill-gray" points="0,0 250,0 228,22 0,22"/>
    <polygon class="fill-orange" points="262,0 492,0 492,22 240,22"/>
    <rect class="fill-gray" x="120" y="84" width="52" height="52"/>
    <text class="brand-name" x="196" y="116">Wrenford</text>
    <text class="brand-tagline" x="198" y="135">Trusted care on local roads</text>

    <path class="connector" d="M163,219 C220,250 280,290 330,314 C280,340 220,375 163,404 C220,430 280,460 330,484"/>

    <rect class="fill-orange" x="205" y="183" width="172" height="48" rx="24"/>
    <text class="value-label" x="232" y="216">PRIDE</text>
    <rect class="fill-orange" x="115" y="288" width="165" height="48" rx="24"/>
    <text class="value-label" x="134" y="321">HONESTY</text>
    <rect class="fill-orange" x="213" y="378" width="164" height="48" rx="24"/>
    <text class="value-label" x="246" y="411">RESPECT</text>
    <rect class="fill-orange" x="115" y="481" width="165" height="48" rx="24"/>
    <text class="value-label" x="130" y="515">DILIGENCE</text>

    <circle class="ring" cx="163" cy="219" r="44"/>
    <circle cx="163" cy="219" r="30" fill="url(#iconTone)" role="img" aria-label="Medal icon"/>
    <circle class="ring" cx="330" cy="314" r="44"/>
    <circle cx="330" cy="314" r="30" fill="url(#iconTone)" role="img" aria-label="Heart with raised hand icon"/>
    <circle class="ring" cx="163" cy="404" r="44"/>
    <circle cx="163" cy="404" r="30" fill="url(#iconTone)" role="img" aria-label="Handshake icon"/>
    <circle class="ring" cx="330" cy="484" r="44"/>
    <circle cx="330" cy="484" r="30" fill="url(#iconTone)" role="img" aria-label="Speech bubbles with gear icon"/>

    <polygon class="fill-orange" points="492,505 492,655 0,655 0,612 380,612"/>
    <polygon class="fill-gray" points="0,561 410,561 372,604 0,604"/>
    <polygon class="fill-white" points="0,604 372,604 365,611 0,611"/>
    <text class="values-title" x="20" y="597">CULTURAL VALUES</text>
    <rect class="frame" x="1.5" y="1.5" width="489" height="652"/>
  </svg>

</main>
</body>
</html>
```